App-Design für Vergleichsportal für Reparaturen
Zielgruppe
Flickwerkstatt ist das Vergleichsportal für Reparaturen in deiner Nähe. Egal ob du eine Werkstatt für dein Smartphone, Tablet, Laptop, Computer, Smartwatch oder Spielkonsole suchst. Mit uns findest du deine passende Reparaturwerkstat in deiner Nähe mit dem besten Preis für dich. Du kannst dich direkt über unser Portal deinen Reparaturauftrag erhalten und wirst durch unser Sicher Kaufen Käuferschutz und unser MONVIRA Treuhandschutz abgesichert.
Aufgabenstellung
Unter Flickwerkstatt.de kann das aktuelle Design angeschaut werden. Die Farbe sollten übernommen werden.
Über die Startseite kann der Kunde sein Gerät, Service sowie seine Adresse eingeben. Auf der Vergleichsseite bekommt der Kunde die Übersicht welche Reparaturwerkstätten es gibt, zu welche Preisen die ausgewählte Dienstleistung angeboten wird. Wenn der Kunde auf den Button 'Jetzt Online Bestpreis buchen' drückt, dann kommt der Kunde in den Warenkorb. Im Warenkorb können noch weitere Dienstleistungen und Produkte dazugebucht werden. Und anschließend kommt der Kunde in die Kasse und kann der Bestellvorgang beenden. Die Benutzerführung sollte einfach sein. Im Fokus steht die Vergleichsseite. Dort sollte der Kunde ca. 4 Werkstätten auf einen Blick sehen können. Könnte ausschauen wie bei Wahlblick9 in der Kategorie Mobilfunk.
Die Vergleichseite sollte auf jeden Fall folgende Elemente enthalten:
- Entfernung zur Werkstatt in Meter bzw. Kilometer
- Logo der Werkstatt
- Name der Werkstatt
- Bewertungssterne der Werkstatt
- Reparaturzeit und Ersatzeilverfügbarkeit
- Reparaturpreis (Platz sollte auch bei Auswahl von 2 Dienstleistungen vorhanden sein)
- Rabattanzeige
- Qualitätssiegel (noch nicht vorhanden)
- Anzeige von Verknappung (z. B. noch 3 Termin frei)
- Qualitätsmerkmale (z. B. 12 Monate Garantie)
Die Merkmale Öffnungszeiten, Adresse, Kostenpflichtige Zusatzleistungen können aus Platzgründen in den Warenkorbseite wandern außer es gibt eine schöne und einfache Lösung.
In der Warenkorbseite kann dazu auch die Wahlblick9 Seite dienen.
Bei allen sollte auf die Benutzerfreundlichkeit geachtet werden.
Bei offenen Frage stehe ich zur Verfügung und freue mich auf viele Designs.
Vielen DANK im Voraus!

```html
<!DOCTYPE html>
<html lang="de">
<head>
<meta charset="utf-8">
<title>Flickwerkstatt – Dienstleistung wählen</title>
<link href="https://fonts.googleapis.com/css2?family=Source+Sans+3:wght@400;600;700&display=swap" rel="stylesheet">
<style>
  :root{
    --stage:#2a2a2a;
    --teal:#1f4759;
    --teal-deep:#1b3f50;
    --green:#7ab530;
    --ink:#2d3b44;
    --dim-bg:#a7aaac;
    --dim-field:#b4b7b9;
    --white:#ffffff;
    --rule:#d9dcde;
  }
  *{box-sizing:border-box;margin:0;padding:0}
  html,body{width:1200px;height:728px;overflow:hidden;background:var(--stage);
    font-family:"Source Sans 3",Arial,sans-serif}
  .screen{position:absolute;left:435px;top:7px;width:330px;height:714px;background:var(--dim-bg);overflow:hidden}
  .abs{position:absolute}
  .status{left:0;top:0;width:330px;height:71px;background:var(--white)}
  .status-time{left:16px;top:4px;font-size:13px;font-weight:600;color:var(--ink)}
  .status-icons{right:12px;top:8px}
  .brand{left:14px;top:37px;display:flex;align-items:center;gap:5px;font-size:15px;font-weight:600;color:var(--teal)}
  .brand-dot{width:10px;height:10px;border-radius:50%;background:var(--green)}
  .menu{right:14px;top:40px}
  .hero{left:0;top:71px;width:330px;height:73px;background:var(--teal);text-align:center;color:var(--green)}
  .hero-title{margin-top:20px;font-size:11px;font-weight:700}
  .hero-sub{margin-top:2px;font-size:8.5px}
  .category{left:25px;top:177px;width:278px;height:39px;background:var(--dim-field);
    color:var(--teal);font-size:12.5px;padding:11px 10px;display:flex;justify-content:space-between}
  .cta-bar{left:25px;top:545px;width:278px;height:28px;background:var(--teal-deep);
    color:#8fa3ad;font-size:9.5px;font-weight:600;text-align:center;padding-top:11px;letter-spacing:.2px}
  .modal{left:25px;top:221px;width:278px;height:335px;background:var(--white);box-shadow:0 2px 6px rgba(0,0,0,.2)}
  .modal-head{height:50px;background:var(--teal);color:var(--white);font-size:13px;padding:16px 16px;
    display:flex;justify-content:space-between;align-items:center}
  .modal-body{padding:15px 17px 0}
  .section-title{font-size:10.5px;color:var(--ink);padding-bottom:6px;border-bottom:1px solid var(--rule)}
  .service{display:flex;align-items:center;height:30.7px;font-size:10px;color:var(--ink)}
  .service:first-of-type{margin-top:6px}
  .service.is-selected{color:var(--green)}
  .service-icon{width:14px;display:flex;justify-content:flex-start}
  .service-name{flex:1}
  .more{display:flex;justify-content:center;align-items:center;gap:5px;margin:15px auto 0;width:179px;height:25px;
    background:var(--green);color:var(--white);font-size:11.5px}
  .trust{top:626px;width:96px;text-align:center;font-size:7.5px;color:var(--ink)}
  .trust svg{display:block;margin:0 auto 4px}
</style>
</head>
<body>
<main class="screen">
  <div class="abs status"></div>
  <div class="abs status-time">9:41</div>
  <svg class="abs status-icons" width="54" height="10" viewBox="0 0 54 10" aria-hidden="true">
    <g fill="#2d3b44"><rect x="0" y="7" width="2" height="3"/><rect x="3" y="5" width="2" height="5"/><rect x="6" y="3" width="2" height="7"/><rect x="9" y="1" width="2" height="9"/></g>
    <path d="M16 4a8 8 0 0 1 11 0M18 6a5 5 0 0 1 7 0" stroke="#2d3b44" stroke-width="1.4" fill="none"/><circle cx="21.5" cy="8.5" r="1.2" fill="#2d3b44"/>
    <rect x="33" y="1" width="18" height="8" rx="2" fill="none" stroke="#2d3b44"/><rect x="35" y="3" width="14" height="4" fill="#2d3b44"/><rect x="52" y="3.5" width="1.5" height="3" fill="#2d3b44"/>
  </svg>
  <div class="abs brand"><span class="brand-dot"></span>Flickwerkstatt</div>
  <svg class="abs menu" width="20" height="14" viewBox="0 0 20 14" aria-label="Menü"><g stroke="#1f4759" stroke-width="1.3"><path d="M0 1h20M0 7h20M0 13h20"/></g></svg>

  <section class="abs hero">
    <p class="hero-title">Reparaturen Im Vergleich, in deiner Nähe!</p>
    <p class="hero-sub">Garantiert die besten Tarife</p>
  </section>

  <div class="abs category"><span>Reparaturkategorie wählen</span>
    <svg width="9" height="6" viewBox="0 0 9 6" style="margin-top:6px"><path d="M1 1l3.5 3.5L8 1" stroke="#7ab530" fill="none"/></svg></div>

  <div class="abs cta-bar">AUF ZUM REPARATURWERKSTATTVERGLEICH &gt;</div>

  <section class="abs modal">
    <header class="modal-head"><span>Dienstleistung wählen</span>
      <svg width="10" height="10" viewBox="0 0 10 10" aria-label="Schließen"><path d="M0 0l10 10M10 0L0 10" stroke="#7ab530" stroke-width="1.2"/></svg></header>
    <div class="modal-body">
      <p class="section-title">Top Dienstleistungen</p>

      <div class="service is-selected"><span class="service-icon"><svg width="6" height="9"><rect x=".5" y=".5" width="5" height="8" rx="1" fill="none" stroke="#7ab530"/></svg></span><span class="service-name">Display Original-Qualität</span>
        <svg width="9" height="9"><circle cx="4.5" cy="4.5" r="4.5" fill="#7ab530"/><path d="M2.3 4.6l1.5 1.4 3-3" stroke="#fff" fill="none"/></svg></div>
      <div class="service"><span class="service-icon"><svg width="6" height="9"><rect x=".5" y=".5" width="5" height="8" rx="1" fill="none" stroke="#7ab530"/></svg></span><span class="service-name">Display Nachbau-Qualität</span>
        <svg width="9" height="9"><circle cx="4.5" cy="4.5" r="4.5" fill="#1f4759"/><path d="M4.5 4v3" stroke="#fff" stroke-width="1.3"/><circle cx="4.5" cy="2.5" r=".7" fill="#fff"/></svg></div>
      <div class="service"><span class="service-icon"><svg width="9" height="9"><path d="M1 8l4-4M5 4a2 2 0 1 1 2.5 1" stroke="#7ab530" stroke-width="1.6" fill="none"/></svg></span><span class="service-name">Backcover (Rückseite)</span>
        <svg width="9" height="9"><circle cx="4.5" cy="4.5" r="4.5" fill="#1f4759"/><path d="M4.5 4v3" stroke="#fff" stroke-width="1.3"/><circle cx="4.5" cy="2.5" r=".7" fill="#fff"/></svg></div>
      <div class="service"><span class="service-icon"><svg width="12" height="7"><rect x=".5" y=".5" width="10" height="6" fill="none" stroke="#7ab530"/><rect x="2" y="2" width="4" height="3" fill="#7ab530"/></svg></span><span class="service-name">Akku</span>
        <svg width="9" height="9"><circle cx="4.5" cy="4.5" r="4.5" fill="#1f4759"/><path d="M4.5 4v3" stroke="#fff" stroke-width="1.3"/><circle cx="4.5" cy="2.5" r=".7" fill="#fff"/></svg></div>
      <div class="service is-selected"><span class="service-icon"><svg width="11" height="8"><path d="M1 3a6.5 6.5 0 0 1 9 0M3 5a3.5 3.5 0 0 1 5 0" stroke="#7ab530" stroke-width="1.3" fill="none"/><circle cx="5.5" cy="7" r="1" fill="#7ab530"/></svg></span><span class="service-name">W-LAN Antenne</span>
        <svg width="9" height="9"><circle cx="4.5" cy="4.5" r="4.5" fill="#7ab530"/><path d="M2.3 4.6l1.5 1.4 3-3" stroke="#fff" fill="none"/></svg></div>
      <div class="service"><span class="service-icon"><svg width="6" height="10"><path d="M1 3l4 4-2 2V1l2 2-4 4" stroke="#7ab530" fill="none"/></svg></span><span class="service-name">Bluetooth Antenne</span>
        <svg width="9" height="9"><circle cx="4.5" cy="4.5" r="4.5" fill="#1f4759"/><path d="M4.5 4v3" stroke="#fff" stroke-width="1.3"/><circle cx="4.5" cy="2.5" r=".7" fill="#fff"/></svg></div>

      <div class="more"><svg width="11" height="11" aria-hidden="true"><g fill="#fff"><circle cx="5.5" cy="1" r="1"/><circle cx="9" cy="3" r="1"/><circle cx="9" cy="8" r="1"/><circle cx="5.5" cy="10" r="1"/><circle cx="2" cy="8" r=".8"/><circle cx="2" cy="3" r=".7"/></g></svg>weitere Dienstleistung</div>
    </div>
  </section>

  <div class="abs trust" style="left:20px">
    <svg width="48" height="56" viewBox="0 0 48 56" aria-hidden="true"><path d="M24 2C17 6 9 8 3 8v20c0 13 10 22 21 26 11-4 21-13 21-26V8c-6 0-14-2-21-6z" fill="none" stroke="#5f8f24" stroke-width="3"/><text x="24" y="38" text-anchor="middle" font-size="22" fill="#1f4759" font-family="Source Sans 3,sans-serif">€</text></svg>
    Käuferschutz</div>
  <div class="abs trust" style="left:116px">
    <svg width="48" height="56" viewBox="0 0 48 56" aria-hidden="true"><path d="M24 2C17 6 9 8 3 8v20c0 13 10 22 21 26 11-4 21-13 21-26V8c-6 0-14-2-21-6z" fill="none" stroke="#5f8f24" stroke-width="3"/><path d="M13 30l6-6 5 3 5-4 6 6-7 7-4-3-4 3z" fill="none" stroke="#1f4759" stroke-width="1.6"/></svg>
    Treuhandschutz</div>
  <div class="abs trust" style="left:213px">
    <svg width="48" height="56" viewBox="0 0 48 56" aria-hidden="true"><path d="M24 2C17 6 9 8 3 8v20c0 13 10 22 21 26 11-4 21-13 21-26V8c-6 0-14-2-21-6z" fill="none" stroke="#5f8f24" stroke-width="3"/><path d="M19 26v-4a5 5 0 0 1 10 0v4" fill="none" stroke="#1f4759" stroke-width="1.8"/><rect x="16" y="26" width="16" height="12" rx="2" fill="none" stroke="#1f4759" stroke-width="1.8"/><circle cx="24" cy="32" r="1.6" fill="#1f4759"/></svg>
    Datenschutz</div>
</main>
</body>
</html>
```